Home show booth design

We are looking at a home show booth design for our window and door company. We will have some high end doors, windows, patio door and garage door on display. 1 booth is 10x20 and 1 booth is 20x20.

Give me some design ideas and keeping in mind our product on display.

Below is our logo and i would like to keep our branding colors and i want a very attractive and high end setup to stand out from the crowd

Target Market(s)

Home owners and custom home builders

Industry/Entity Type

Windows and doors

Font styles to use
Serif

Colors

Designer to choose colors to be used in the design.

Requirements
Must have
• Back drop, small desk
Nice to have
• Large floating balloon above the booth

```html
<!DOCTYPE html>
<html lang="en">
<head>
<meta charset="utf-8">
<title>Lintel Doors &amp; Windows – Home Show Booth Graphics</title>
<link rel="stylesheet" href="https://fonts.googleapis.com/css2?family=Outfit:wght@400;500;700&display=swap">
<style>
  :root{
    --stage:#8e8e8e;
    --white:#ffffff;
    --charcoal:#2b2a29;
    --charcoal-soft:#3a3836;
    --orange:#e8742a;
    --orange-deep:#b9561b;
    --grey-text:#4a4744;
    --sky:#8fb4d6;
    --lawn:#5f9a3a;
    --stone:#9a8f84;
    --dusk:#c98a5a;
  }
  *{margin:0;padding:0;box-sizing:border-box}
  html,body{width:843px;height:1200px;overflow:hidden;background:var(--stage)}
  body{font-family:"Outfit",sans-serif;position:relative}
  .panel{position:absolute;box-shadow:0 6px 14px rgba(0,0,0,.25);background:var(--white)}
  .panel svg{display:block;width:100%;height:100%}
  .backdrop-main{left:20px;top:210px;width:525px;height:525px}
  .backdrop-side{left:559px;top:210px;width:263px;height:525px}
  .counter-wrap{left:228px;top:790px;width:386px;height:190px}
  .brand-name{font-weight:700;fill:var(--orange)}
  .brand-tag{font-weight:500;fill:var(--grey-text)}
  .headline-accent{font-weight:700;fill:var(--orange)}
  .headline{font-weight:500;fill:var(--white)}
  .label{font-weight:400;fill:var(--white)}
  .url{font-weight:500;fill:var(--white)}
</style>
</head>
<body>

<!-- Main backdrop panel -->
<div class="panel backdrop-main">
  <svg viewBox="0 0 709 710" xmlns="http://www.w3.org/2000/svg">
    <defs>
      <linearGradient id="nightHouse" x1="0" y1="0" x2="0" y2="1">
        <stop offset="0" stop-color="#3a3938"/>
        <stop offset="1" stop-color="#242322"/>
      </linearGradient>
      <clipPath id="heroClip">
        <circle cx="532" cy="185" r="130"/>
      </clipPath>
    </defs>
    <rect width="709" height="710" fill="var(--white)"/>
    <path d="M0 290 C200 170 430 120 709 112 V710 H0Z" fill="var(--orange)"/>
    <path d="M0 304 C200 186 430 136 709 128 V710 H0Z" fill="url(#nightHouse)" role="img" aria-label="Dimmed evening photo of a modern home behind the headline"/>

    <rect x="46" y="52" width="88" height="88" fill="none" stroke="var(--charcoal)" stroke-width="8"/>
    <text class="brand-name" x="150" y="104" font-size="30">LINTEL</text>
    <text class="brand-tag" x="150" y="127" font-size="15">— Doors &amp; Windows —</text>

    <circle cx="532" cy="185" r="152" fill="var(--orange)"/>
    <circle cx="532" cy="185" r="136" fill="var(--white)"/>
    <g clip-path="url(#heroClip)" role="img" aria-label="Photo of a contemporary two-storey home with wood cladding and lawn">
      <rect x="402" y="55" width="260" height="260" fill="var(--sky)"/>
      <rect x="402" y="235" width="260" height="80" fill="var(--lawn)"/>
    </g>

    <text class="headline-accent" x="46" y="330" font-size="38">Elevate Your Home</text>
    <text class="headline" x="46" y="376" font-size="38">With Lintel Doors</text>
    <text class="headline" x="46" y="422" font-size="38">&amp; Windows</text>

    <g>
      <path d="M64 560 A95 95 0 0 0 254 560 Z" fill="var(--orange-deep)" opacity=".55"/>
      <circle cx="159" cy="525" r="76" fill="var(--orange)"/>
      <circle cx="159" cy="525" r="66" fill="#d9d6d2" role="img" aria-label="Photo of a patio door in a bright entry hall"/>
      <text class="label" x="159" y="648" font-size="17" text-anchor="middle">Patio Doors</text>
    </g>
    <g>
      <path d="M259 560 A95 95 0 0 0 449 560 Z" fill="var(--orange-deep)" opacity=".55"/>
      <circle cx="354" cy="525" r="76" fill="var(--orange)"/>
      <circle cx="354" cy="525" r="66" fill="#3d4a63" role="img" aria-label="Photo of a modern home with a garage door at dusk"/>
      <text class="label" x="354" y="648" font-size="17" text-anchor="middle">Garage Doors</text>
    </g>
    <g>
      <path d="M454 560 A95 95 0 0 0 644 560 Z" fill="var(--orange-deep)" opacity=".55"/>
      <circle cx="549" cy="525" r="76" fill="var(--orange)"/>
      <circle cx="549" cy="525" r="66" fill="var(--dusk)" role="img" aria-label="Photo of a house with many windows at sunset"/>
      <text class="label" x="549" y="648" font-size="17" text-anchor="middle">Windows</text>
    </g>
  </svg>
</div>

<!-- Side backdrop panel -->
<div class="panel backdrop-side">
  <svg viewBox="0 0 355 710" xmlns="http://www.w3.org/2000/svg">
    <rect width="355" height="710" fill="var(--white)"/>
    <rect width="355" height="170" fill="#6f6a5c" role="img" aria-label="Photo of a traditional gabled house at dusk"/>
    <path d="M0 140 C120 150 250 190 355 250 V710 H0Z" fill="var(--orange)"/>
    <path d="M0 154 C120 164 250 204 355 266 V710 H0Z" fill="var(--charcoal)"/>

    <circle cx="178" cy="245" r="110" fill="var(--orange)"/>
    <circle cx="178" cy="245" r="98" fill="var(--white)"/>
    <circle cx="178" cy="245" r="93" fill="var(--stone)" role="img" aria-label="Photo of a grey front entry door with decorative glass"/>

    <text class="label" x="178" y="384" font-size="17" text-anchor="middle">We craft them <tspan class="headline-accent">in-house</tspan></text>
    <text class="label" x="178" y="406" font-size="17" text-anchor="middle">to meet the highest standards</text>
    <text class="label" x="178" y="428" font-size="17" text-anchor="middle">of quality.</text>

    <path d="M0 560 C120 500 250 460 355 445 V710 H0Z" fill="var(--orange)"/>
    <path d="M0 576 C120 516 250 476 355 462 V710 H0Z" fill="var(--white)"/>

    <circle cx="117" cy="530" r="80" fill="var(--orange)"/>
    <circle cx="117" cy="530" r="70" fill="var(--white)"/>
    <circle cx="117" cy="530" r="66" fill="#8a7f70" role="img" aria-label="Photo of a modern stone house entrance with a dark door"/>

    <rect x="247" y="500" width="50" height="50" fill="none" stroke="var(--charcoal)" stroke-width="6"/>
    <text class="brand-name" x="272" y="590" font-size="22" text-anchor="middle">LINTEL</text>
    <text class="brand-tag" x="272" y="607" font-size="11" text-anchor="middle">— Doors &amp; Windows —</text>

    <rect x="40" y="634" width="275" height="28" rx="14" fill="var(--orange)"/>
    <text class="url" x="178" y="654" font-size="16" text-anchor="middle">www.linteldoors.example</text>
  </svg>
</div>

<!-- Counter wrap -->
<div class="panel counter-wrap">
  <svg viewBox="0 0 386 190" xmlns="http://www.w3.org/2000/svg">
    <rect width="386" height="190" fill="var(--white)"/>
    <path d="M0 190 V165 C100 115 290 115 386 165 V190Z" fill="var(--orange)"/>
    <path d="M0 190 V174 C100 126 290 126 386 174 V190Z" fill="var(--charcoal)"/>

    <rect x="46" y="42" width="24" height="24" fill="none" stroke="var(--charcoal)" stroke-width="3"/>
    <text class="brand-name" x="58" y="86" font-size="11" text-anchor="middle">LINTEL</text>
    <text class="brand-tag" x="58" y="95" font-size="6" text-anchor="middle">— Doors &amp; Windows —</text>

    <rect x="175" y="24" width="36" height="36" fill="none" stroke="var(--charcoal)" stroke-width="4"/>
    <text class="brand-name" x="193" y="84" font-size="15" text-anchor="middle">LINTEL</text>
    <text class="brand-tag" x="193" y="96" font-size="7.5" text-anchor="middle">— Doors &amp; Windows —</text>

    <text class="url" x="193" y="163" font-size="7" text-anchor="middle">www.linteldoors.example</text>
  </svg>
</div>

</body>
</html>
```